Gardener needs an exciting new flyer design.

I'm a passionate gardener that requires a custom flyer design for a owner operator gardening business. Design will be for a DL flyer. I'm based on the Sunshine coast in Queensland Australia. My target audience is the residential market on the Sunshine coast. Business name is Marlowe Greens. My services are, lawn mowing, weeding, Eco Friendly fertilizing, green waste removal, Mulching, tree and shrub pruning, Full garden makeovers, hedging, pressure cleaning, privacy screening, Timber deck rejuvenation, Planting, Turf preparation and installation, and much more. Free no obligation quotes, reliable and friendly service, great rates. 12 years experience. Web www.marlowegreens.com.au - Phone 0418527064 - Email doug@marlowegreens.com.au I would like the design to portray a friendly and professional approach.

Target Market(s)

Residential

Industry/Entity Type

Gardener

Font styles to use
Serif

Colors
9ccb3b
abd037
3176b5

Requirements
Must have
• my services, my logo, my contact details,

```html
<!DOCTYPE html>
<html lang="en">
<head>
<meta charset="utf-8">
<title>Marlowe Greens – DL Flyer</title>
<link href="https://fonts.googleapis.com/css2?family=Alegreya+Sans:wght@700&family=Oswald:wght@500&family=Roboto+Condensed:wght@300;400&family=Alegreya:wght@700&display=swap" rel="stylesheet">
<style>
  :root{
    --page:#1f8f3f;
    --forest:#175e30;
    --forest-deep:#0e3f1f;
    --lime:#a6cf3a;
    --lime-soft:#c4dd5a;
    --white:#ffffff;
    --ink-green:#124a24;
  }
  html,body{margin:0;padding:0;width:1124px;height:1200px;overflow:hidden;background:var(--page);}
  .flyer{position:absolute;left:296px;top:36px;width:531px;height:1128px;background:var(--forest);overflow:hidden;}
  .flyer-shapes{position:absolute;inset:0;}
  .brand{position:absolute;left:340px;top:78px;width:190px;display:flex;align-items:center;gap:8px;
    font-family:"Alegreya Sans",sans-serif;font-weight:700;font-size:21px;color:var(--ink-green);}
  .brand-dot{width:12px;height:12px;border-radius:50%;background:var(--lime);}
  .headline{position:absolute;left:33px;top:598px;margin:0;font-family:"Alegreya Sans",sans-serif;
    font-weight:700;font-size:41px;line-height:48px;color:var(--white);}
  .offer{position:absolute;left:39px;top:840px;margin:0;font-family:"Oswald",sans-serif;font-weight:500;
    font-size:17px;line-height:25px;color:var(--lime);text-transform:uppercase;}
  .experience{position:absolute;left:39px;top:940px;margin:0;font-family:"Oswald",sans-serif;font-weight:500;
    font-size:17px;color:var(--lime);text-transform:uppercase;}
  .contact{position:absolute;left:39px;top:995px;margin:0;padding:0;list-style:none;
    font-family:"Roboto Condensed",sans-serif;font-weight:300;font-size:15px;line-height:23px;color:var(--white);}
  .contact li{display:flex;align-items:center;gap:8px;}
  .divider{position:absolute;left:286px;top:743px;width:1px;height:293px;background:rgba(166,207,58,.55);}
  .services{position:absolute;left:313px;top:734px;margin:0;padding:0;list-style:none;
    font-family:"Roboto Condensed",sans-serif;font-weight:400;font-size:15.5px;line-height:21.7px;color:var(--white);}
  .services li{display:flex;align-items:center;gap:7px;}
  .leaf{width:11px;height:6px;border-radius:0 100% 0 100%;background:var(--lime);transform:rotate(20deg);flex:none;}
  .web{position:absolute;left:0;top:1090px;width:531px;height:24px;background:var(--white);
    font-family:"Alegreya",serif;font-weight:700;font-size:16px;line-height:24px;text-align:center;color:var(--ink-green);}
</style>
</head>
<body>
<main class="flyer">
  <svg class="flyer-shapes" width="531" height="1128" viewBox="0 0 531 1128">
    <defs>
      <linearGradient id="gardenTones" x1="0" y1="0" x2="1" y2="1">
        <stop offset="0" stop-color="#4e7a35"/>
        <stop offset=".35" stop-color="#d9c23a"/>
        <stop offset=".6" stop-color="#5f9c3a"/>
        <stop offset="1" stop-color="#3f8a2a"/>
      </linearGradient>
      <linearGradient id="headlineZone" x1="0" y1="0" x2="0" y2="1">
        <stop offset="0" stop-color="#1b6434"/>
        <stop offset="1" stop-color="#0d3b1d"/>
      </linearGradient>
      <linearGradient id="lowerZone" x1="0" y1="0" x2="0" y2="1">
        <stop offset="0" stop-color="#1a5f31"/>
        <stop offset="1" stop-color="#12472a"/>
      </linearGradient>
      <linearGradient id="grassTones" x1="0" y1="0" x2="0" y2="1">
        <stop offset="0" stop-color="#2c6a2a" stop-opacity="0"/>
        <stop offset=".5" stop-color="#b7d640"/>
        <stop offset="1" stop-color="#7fb52f"/>
      </linearGradient>
    </defs>
    <rect class="lower-field" x="0" y="600" width="531" height="528" fill="url(#lowerZone)"/>
    <path class="headline-field" d="M0,499 C150,580 380,610 531,604 L531,604 C470,660 390,760 0,773 Z" fill="url(#headlineZone)"/>
    <path class="garden-photo" role="img" aria-label="Photo of a lush flowering garden with a white chair on green lawn"
          d="M0,0 H531 V581 C380,585 150,540 0,415 Z" fill="url(#gardenTones)"/>
    <path class="brand-corner" d="M266,0 H531 V165 C420,165 320,100 266,0 Z" fill="#ffffff"/>
    <path class="lime-band" d="M0,415 C150,540 380,585 531,581 V604 C380,610 150,580 0,499 Z" fill="#a6cf3a"/>
    <rect class="grass-strip" role="img" aria-label="Illustrated blades of bright green grass" x="0" y="1045" width="531" height="45" fill="url(#grassTones)"/>
    <rect class="grass-base" role="img" aria-label="Grass edge" x="0" y="1114" width="531" height="14" fill="#9cc83a"/>
  </svg>

  <div class="brand"><span class="brand-dot"></span>Marlowe Greens</div>

  <h1 class="headline">A beautiful garden<br>doesn't happen<br>by itself</h1>

  <p class="offer">Free no obligation quotes,<br>reliable and friendly<br>service, great rates.</p>
  <p class="experience">12 years experience.</p>

  <ul class="contact">
    <li>
      <svg width="15" height="15" viewBox="0 0 16 16"><circle cx="8" cy="8" r="8" fill="#a6cf3a"/><path d="M5 4.5c.5-.5 1-.5 1.3 0l.7 1.3c.2.4 0 .7-.3 1l-.3.3c.4.9 1.2 1.7 2.1 2.1l.3-.3c.3-.3.6-.5 1-.3l1.3.7c.5.3.5.8 0 1.3-.8.8-2 .9-3 .3C6.3 10.1 5.4 9.2 4.8 8c-.6-1-.5-2.7.2-3.5z" fill="#175e30"/></svg>
      0418527064
    </li>
    <li>
      <svg width="15" height="12" viewBox="0 0 16 12"><rect x="0" y="2" width="16" height="10" fill="#a6cf3a"/><path d="M0 2 L8 7 L16 2 L8 0 Z" fill="#c4dd5a"/><path d="M0 2 L8 7 L16 2" fill="none" stroke="#175e30" stroke-width="1"/></svg>
      doug@marlowegreens.com.au
    </li>
  </ul>

  <div class="divider"></div>

  <ul class="services">
    <li><span class="leaf"></span>Lawn mowing</li>
    <li><span class="leaf"></span>Weeding</li>
    <li><span class="leaf"></span>Eco Friendly fertilizing</li>
    <li><span class="leaf"></span>Green waste removal</li>
    <li><span class="leaf"></span>Mulching</li>
    <li><span class="leaf"></span>Tree &amp; shrub pruning</li>
    <li><span class="leaf"></span>Full garden makeovers</li>
    <li><span class="leaf"></span>Hedging</li>
    <li><span class="leaf"></span>Pressure cleaning</li>
    <li><span class="leaf"></span>Privacy screening</li>
    <li><span class="leaf"></span>Timber deck rejuvenation</li>
    <li><span class="leaf"></span>Planting</li>
    <li><span class="leaf"></span>Turf preparation &amp; installation</li>
    <li><span class="leaf"></span>And much more.</li>
  </ul>

  <div class="web">www.marlowegreens.com.au</div>
</main>
</body>
</html>
```